ADVERT DESIGN FOR INTERNATIONAL PAYMENTS COMPANY

Looking to design an advert for our business. We specialise in selling FX and making international payments.
Advert should come across as professional and discreet
Points to note are,
Authorised by DWTV and the PSJ
Bank-Beating Exchange Rates
0% Commission
UK Office: 47 Morbury Terrace London SE9 4QT
Gibraltar Office: Suite 5B Tallow Court 8 Pennick Steps Gibraltar GX24 7BT
E: desk@wrenpaybx.co.uk
T: 020 73914486
There shouldn't be any other text. As a suggestion the background image should perhaps be reminiscent of our ability to make payments across the word quickly and securely. But other ideas welcome.

```html
<!DOCTYPE html>
<html lang="en">
<head>
<meta charset="utf-8">
<title>Wrenpay – International Payments Advert</title>
<link rel="stylesheet" href="https://fonts.googleapis.com/css2?family=Poppins:wght@300;400;600;700&display=swap">
<style>
  :root {
    --navy-deep: #070b24;
    --navy: #0f1838;
    --navy-glow: #1c2550;
    --light-glow: rgba(214, 190, 140, 0.18);
    --white: #ffffff;
  }
  html, body {
    margin: 0;
    padding: 0;
    width: 1200px;
    height: 1200px;
    overflow: hidden;
    background: var(--navy-deep);
  }
  .advert {
    position: relative;
    width: 1200px;
    height: 1200px;
    overflow: hidden;
    font-family: "Poppins", sans-serif;
    color: var(--white);
  }
  .backdrop {
    position: absolute;
    inset: 0;
    background:
      radial-gradient(ellipse 420px 300px at 78% 62%, var(--light-glow), transparent 70%),
      radial-gradient(ellipse 300px 260px at 18% 48%, rgba(214, 190, 140, 0.1), transparent 70%),
      radial-gradient(ellipse 700px 600px at 55% 45%, var(--navy-glow), transparent 75%),
      linear-gradient(160deg, var(--navy) 0%, var(--navy-deep) 100%);
  }
  .brand {
    position: absolute;
    left: 97px;
    top: 96px;
    display: flex;
    align-items: center;
    gap: 12px;
    font-weight: 600;
    font-size: 40px;
    letter-spacing: -0.5px;
    line-height: 1;
  }
  .brand-dot {
    width: 14px;
    height: 14px;
    border-radius: 50%;
    background: var(--white);
  }
  .headline-block {
    position: absolute;
    left: 0;
    right: 0;
    top: 240px;
    text-align: center;
  }
  .authorisation {
    margin: 0;
    font-weight: 400;
    font-size: 32px;
    line-height: 42px;
  }
  .headline {
    margin: 22px 0 0;
    font-weight: 600;
    font-size: 76px;
    line-height: 68px;
    letter-spacing: -0.5px;
  }
  .commission {
    margin: 38px 0 0;
    font-weight: 600;
    font-size: 76px;
    line-height: 80px;
    letter-spacing: -0.5px;
  }
  .offices {
    position: absolute;
    left: 97px;
    top: 940px;
    font-size: 22px;
    line-height: 29.5px;
    font-weight: 300;
  }
  .offices svg { display: block; margin-bottom: 12px; }
  .office-label { font-weight: 600; display: block; }
  .office-address { display: block; }
  .contacts {
    position: absolute;
    left: 843px;
    top: 1008px;
    font-size: 22px;
    font-weight: 300;
  }
  .contact-row {
    display: flex;
    align-items: center;
    gap: 18px;
    height: 34px;
    margin-bottom: 25px;
  }
  .contact-row svg { flex: none; }
</style>
</head>
<body>
<main class="advert">
  <div class="backdrop" role="img" aria-label="Night-time satellite view of a continent with glowing city lights"></div>

  <div class="brand"><span class="brand-dot"></span>Wrenpay</div>

  <section class="headline-block">
    <p class="authorisation">Authorised by DWTV and the PSJ</p>
    <h1 class="headline">Bank-Beating<br>Exchange Rates</h1>
    <p class="commission">0% Commission</p>
  </section>

  <section class="offices">
    <svg width="18" height="22" viewBox="0 0 18 22" fill="none" stroke="#fff" stroke-width="1.4">
      <path d="M9 21s7-7.2 7-12.2A7 7 0 0 0 2 8.8C2 13.8 9 21 9 21z"/>
      <circle cx="9" cy="8.8" r="2.6"/>
    </svg>
    <span class="office-label">UK Office:</span>
    <span class="office-address">47 Morbury Terrace London SE9 4QT</span>
    <span class="office-label">Gibraltar Office:</span>
    <span class="office-address">Suite 5B Tallow Court 8 Pennick Steps Gibraltar GX24 7BT</span>
  </section>

  <section class="contacts">
    <div class="contact-row">
      <svg width="22" height="17" viewBox="0 0 22 17" fill="none" stroke="#fff" stroke-width="1.4">
        <rect x="1" y="1" width="20" height="15" rx="1"/>
        <path d="M1 1l10 8 10-8M1 16l7-7M21 16l-7-7"/>
      </svg>
      <span>desk@wrenpaybx.co.uk</span>
    </div>
    <div class="contact-row">
      <svg width="22" height="22" viewBox="0 0 22 22" fill="none" stroke="#fff" stroke-width="1.4">
        <path d="M5 2l3 4-2 2.5c1 2.5 3 4.5 5.5 5.5L14 12l4 3-1.5 3.5C10 18 4 12 3.5 5.5z"/>
        <path d="M13 3a6 6 0 0 1 6 6M13 6.5a2.5 2.5 0 0 1 2.5 2.5"/>
      </svg>
      <span>020 73914486</span>
    </div>
  </section>
</main>
</body>
</html>
```